Design interface for an invoicing software

We are developing a new invoicing software that is a very boring topic. Users can use the software to write invoices and manage their income. Therefore we want to inspire the users with a great desgin. By this we mean, for example, the use of photos in the background (streets in New York, landscapes), or "crazy" looking headlines or something else. Target group are young start-ups, freelancers, hairdressers and taxi drivers at the age of 18-40 years. It would also be worth considering to adapt the look to the user's industry. However, the menu items themselves and the approximate position of the information are given. See file "startpoint" What kind of ideas do you have?

Target Market(s)

Europe

Industry/Entity Type

Small Business

Colors

Designer to choose colors to be used in the design.

Requirements
Must have
• the menu items themselves and the approximate position of the information are given. The navigation menu itself can be different.
Should not have
• boring look and feel

```html
<!DOCTYPE html>
<html lang="en">
<head>
<meta charset="utf-8">
<title>Invoicing App – Menu and Dashboard</title>
<link rel="stylesheet" href="https://fonts.googleapis.com/css2?family=Montserrat:wght@700&family=Poppins:wght@300;400;600&display=swap">
<style>
:root{
  --page:#ffffff;
  --title:#8c8c8c;
  --subtitle:#b4b4b4;
  --ink-black:#000000;
  --menu-text:#dcdcdc;
  --bar-light:#ecebe6;
  --navy:#2f3447;
  --photo-a:#c9cfc4;
  --photo-b:#8f9c98;
  --card:#4b4c58;
  --card-line:#5a5b67;
  --card-text:#e6e6ea;
  --card-muted:#7d7e8a;
  --stats:#2c2c32;
  --plum:#4f3a58;
  --cyan:#2ab7d8;
  --pink:#e4306f;
}
*{margin:0;padding:0;box-sizing:border-box}
html,body{width:1200px;height:1200px;overflow:hidden;background:var(--page)}
body{position:relative;font-family:"Poppins",sans-serif}

.section-head{position:absolute}
.section-head h1{font-family:"Montserrat",sans-serif;font-weight:700;font-size:38px;letter-spacing:2px;color:var(--title);line-height:1}
.section-head p{margin-top:26px;font-weight:300;font-size:16px;letter-spacing:1.4px;line-height:21px;color:var(--subtitle)}
.head-menu{left:206px;top:214px}
.head-dash{left:755px;top:218px}

.screen{position:absolute;width:339px;height:602px;top:406px;overflow:hidden}
.screen-menu{left:186px;background:var(--ink-black);box-shadow:0 40px 50px -20px rgba(60,60,40,.35)}
.screen-dash{left:690px;box-shadow:0 30px 50px -20px rgba(40,40,60,.35)}

.portrait{position:absolute;left:0;top:120px;width:212px;height:482px;
  background:radial-gradient(ellipse at 35% 55%,#2a2a2a 0%,#151515 45%,#000 80%)}

.status{position:absolute;left:0;top:0;width:100%;height:22px;font-size:10px;font-weight:600;display:flex;align-items:center;justify-content:space-between;padding:0 6px}
.status-dark{color:#fff}
.status .time{position:absolute;left:50%;transform:translateX(-60%)}
.status .right{display:flex;align-items:center;gap:4px}
.back-arrow{position:absolute;left:18px;top:56px}

.menu-list{position:absolute;left:0;top:100px;list-style:none}
.menu-item{height:62.6px;display:flex;align-items:center;color:var(--menu-text);font-size:14.5px;letter-spacing:1.3px}
.menu-item svg{width:20px;height:20px;margin-left:23px;margin-right:22px;stroke:var(--menu-text);fill:none;stroke-width:1.6}

.dash-clip{position:absolute;left:212px;top:79px;width:127px;height:523px;overflow:hidden}

.dashboard{position:relative;width:339px;height:602px;background:var(--bar-light);overflow:hidden}
.dash-clip .dashboard{height:523px}
.dash-top{position:relative;height:66px;background:var(--bar-light)}
.dash-top .status{color:#222;font-size:9px}
.hamburger{position:absolute;left:16px;top:50px}
.dash-title{position:absolute;left:125px;top:42px;font-family:"Montserrat",sans-serif;font-weight:700;font-size:18px;letter-spacing:2.5px;color:var(--navy)}
.invoices-area{position:absolute;left:0;top:66px;width:100%;height:262px;
  background:linear-gradient(100deg,var(--photo-a) 0%,#b8c0b6 45%,var(--photo-b) 100%)}
.invoices-label{position:absolute;left:27px;top:18px;font-weight:300;font-size:14px;letter-spacing:.8px;color:#4a4e58}
.invoice-card{position:absolute;left:10px;top:44px;width:319px;height:218px;background:var(--card);border-radius:10px 10px 0 0;padding:0 16px}
.invoice-table{width:100%;border-collapse:collapse;font-size:9px;letter-spacing:.6px;color:var(--card-text)}
.invoice-table th{font-weight:400;color:var(--card-muted);text-align:left;height:32px;padding-top:6px}
.invoice-table td{height:37px;border-top:1px solid var(--card-line)}
.invoice-table .amount{font-weight:600}
.stats{position:absolute;left:0;top:328px;width:100%;height:274px;background:var(--stats)}
.stats h2{position:absolute;left:16px;top:18px;font-weight:300;font-size:14px;color:#d8d8de;letter-spacing:.3px}
.stats-tabs{position:absolute;left:16px;top:45px;display:flex;gap:24px;font-size:9px;letter-spacing:.6px;color:#6e6e78;list-style:none}
.stats-tabs .active{color:#e0e0e6}
.stats-chart{position:absolute;left:0;top:78px;width:339px;height:196px}
</style>
</head>
<body>

<header class="section-head head-menu">
  <h1>Menu</h1>
  <p>Menu screen for<br>your app</p>
</header>
<header class="section-head head-dash">
  <h1>Dashboard</h1>
  <p>Menu screen for<br>your app</p>
</header>

<!-- Menu screen with dashboard sliding behind -->
<section class="screen screen-menu">
  <div class="portrait" role="img" aria-label="Dark black-and-white portrait photograph fading into the background"></div>
  <div class="status status-dark">
    <span>▂▃▅ GS</span>
    <span class="time">9:41 AM</span>
    <span class="right">58 % <svg width="20" height="9"><rect x=".5" y=".5" width="17" height="8" rx="1.5" fill="none" stroke="#fff"/><rect x="2" y="2" width="9" height="5" fill="#fff"/></svg></span>
  </div>
  <svg class="back-arrow" width="24" height="12" viewBox="0 0 24 12"><path d="M23 6H2M7 1 2 6l5 5" stroke="#fff" stroke-width="1.6" fill="none"/></svg>

  <ul class="menu-list">
    <li class="menu-item"><svg viewBox="0 0 20 20"><path d="M2 2v16h16M6 15V9M10 15V6M14 15v-4"/></svg>Dashboard</li>
    <li class="menu-item"><svg viewBox="0 0 20 20"><path d="M5 2h7l4 4v12H5zM12 2v4h4"/></svg>Invoices</li>
    <li class="menu-item"><svg viewBox="0 0 20 20"><circle cx="10" cy="6" r="3.5" fill="#dcdcdc"/><path d="M3 17c0-4 3-6 7-6s7 2 7 6z" fill="#dcdcdc"/></svg>Contacts</li>
    <li class="menu-item"><svg viewBox="0 0 20 20"><path d="M1 3h3l2 10h10l2-7H6"/><circle cx="8" cy="17" r="1"/><circle cx="15" cy="17" r="1"/></svg>Products</li>
    <li class="menu-item"><svg viewBox="0 0 20 20"><rect x="2" y="2" width="16" height="16"/><path d="M7 7h2v2H7zM11 7h2v2h-2zM7 11h2v2H7zM11 11h2v2h-2z"/></svg>Banking</li>
    <li class="menu-item"><svg viewBox="0 0 20 20"><path d="M2 5h16v13H2zM2 5l12-3v3M12 10h6v4h-6z"/></svg>Expenses</li>
    <li class="menu-item"><svg viewBox="0 0 20 20"><path d="M3 17l4-8 4 5 5-10"/><circle cx="3" cy="17" r="1.3"/><circle cx="7" cy="9" r="1.3"/><circle cx="11" cy="14" r="1.3"/><circle cx="16" cy="4" r="1.3"/></svg>Reports</li>
  </ul>

  <div class="dash-clip">
    <div class="dashboard">
      <div class="dash-top">
        <div class="status"><span>▂▃▅ GS</span></div>
        <svg class="hamburger" width="16" height="10"><path d="M0 1h16M0 5h12M0 9h9" stroke="#6b7390" stroke-width="1.3"/></svg>
        <span class="dash-title">Dashboard</span>
      </div>
      <div class="invoices-area" role="img" aria-label="Soft photograph background behind the invoices list">
        <span class="invoices-label">invoices</span>
        <div class="invoice-card">
          <table class="invoice-table">
            <tr><th>Customer</th><th>Amount</th></tr>
            <tr><td>Lena Marsh</td><td class="amount">$ 264.00</td></tr>
            <tr><td>Tom Akers</td><td class="amount">$ 127.80</td></tr>
            <tr><td>Paul Rowe</td><td class="amount">$ 56.05</td></tr>
            <tr><td>Lena Marsh</td><td class="amount">$ 56.05</td></tr>
            <tr><td>Tom Akers</td><td class="amount">$ 56.05</td></tr>
          </table>
        </div>
      </div>
      <div class="stats">
        <h2>statistics</h2>
        <ul class="stats-tabs"><li class="active">Year</li><li>Month</li><li>Week</li></ul>
        <svg class="stats-chart" viewBox="0 0 339 196">
          <path d="M0 110C30 80 60 75 100 90S150 140 190 120 260 95 339 105V196H0z" fill="var(--plum)"/>
          <path d="M0 40C30 60 50 90 80 70S115 30 150 60" stroke="var(--pink)" stroke-width="1.8" fill="none"/>
          <path d="M0 55C30 90 60 80 90 50S130 30 160 55" stroke="var(--cyan)" stroke-width="1.8" fill="none"/>
        </svg>
      </div>
    </div>
  </div>
</section>

<!-- Dashboard screen -->
<section class="screen screen-dash">
  <div class="dashboard">
    <div class="dash-top">
      <div class="status"><span>▂▃▅ GS</span><span class="time">9:41 AM</span><span class="right">58 %</span></div>
      <svg class="hamburger" width="16" height="10"><path d="M0 1h16M0 5h12M0 9h9" stroke="#6b7390" stroke-width="1.3"/></svg>
      <span class="dash-title">Dashboard</span>
    </div>
    <div class="invoices-area" role="img" aria-label="Soft photograph background behind the invoices list">
      <span class="invoices-label">invoices</span>
      <div class="invoice-card">
        <table class="invoice-table">
          <tr><th>Customer</th><th>Amount</th><th>Date</th><th>Due Date</th></tr>
          <tr><td>Lena Marsh</td><td class="amount">$ 264.00</td><td>17.09.2018</td><td>25.09.2018</td></tr>
          <tr><td>Tom Akers</td><td class="amount">$ 127.80</td><td>12.09.2018</td><td>28.09.2018</td></tr>
          <tr><td>Paul Rowe</td><td class="amount">$ 56.05</td><td>05.09.2018</td><td>11.09.2018</td></tr>
          <tr><td>Lena Marsh</td><td class="amount">$ 56.05</td><td>05.09.2018</td><td>11.09.2018</td></tr>
          <tr><td>Tom Akers</td><td class="amount">$ 56.05</td><td>05.09.2018</td><td>11.09.2018</td></tr>
        </table>
      </div>
    </div>
    <div class="stats">
      <h2>statistics</h2>
      <ul class="stats-tabs"><li class="active">Year</li><li>Month</li><li>Week</li></ul>
      <svg class="stats-chart" viewBox="0 0 339 196">
        <path d="M0 40C20 90 40 100 70 85S110 110 130 130 190 170 240 160 300 140 339 135V196H0z" fill="var(--plum)"/>
        <path d="M0 40C10 70 40 70 70 60S110 100 130 110 180 170 230 165 300 150 339 140" stroke="var(--pink)" stroke-width="1.8" fill="none"/>
        <path d="M0 20C10 60 40 80 70 70S110 40 140 80 190 165 250 155 310 140 339 128" stroke="var(--cyan)" stroke-width="1.8" fill="none"/>
      </svg>
    </div>
  </div>
</section>

</body>
</html>
```